Brochure for Community-Based Therapy Company

Will be given out to patients, doctors, case managers. We are redesigning our marketing materials and would like a design for a brochure. We provide therapy to individuals who have been injured in car accidents or on the job. We provide occupational therapy, speech therapy and psychotherapy. We would like the brochure to utilize our corporate ID and color scheme that we are using for our other materials (see attached letterhead and logo).

Stock photos that are used should stay away from images of outpatient or hospital settings, stay away from photos with obvious disabilities (wheelchairs, learning to walk, etc), and nothing that looks like physical therapy, as we don't provide physical therapy only OT, Speech and psychotherapy. Would prefer to not have people wearing masks, as we will use this beyond the pandemic. Also, our staff wears business casual clothing so would prefer photos that the individuals are not wearing scrubs or other medical attire (lab coats, etc).

Target Market(s)

Patients, Physicians/Doctors, Case Managers

Industry/Entity Type

Healthcare

Requirements
Must have
• Prefer a booklet format but doesn't have to be 8.5 inch by 11 inch (can be a little smaller).

```html
<!DOCTYPE html>
<html lang="en">
<head>
<meta charset="utf-8">
<title>Meridian Rehab Partners – Brochure</title>
<link rel="stylesheet" href="https://fonts.googleapis.com/css2?family=Montserrat:wght@500;600;700&family=Open+Sans:wght@400;600&display=swap">
<style>
:root{
  --teal:#6fa797;
  --teal-dark:#5b9583;
  --teal-soft:#e6f0ec;
  --slate:#5f6165;
  --ink:#3a3c40;
  --paper:#ffffff;
  --paper-grey:#efefef;
  --stage:#e3e3e6;
}
*{box-sizing:border-box;margin:0;padding:0}
html,body{width:900px;height:1200px;overflow:hidden}
body{background:var(--stage);font-family:"Open Sans",Arial,sans-serif;color:var(--ink);position:relative}
.spread{position:absolute;left:40px;width:820px;height:540px;display:flex;box-shadow:0 6px 18px rgba(0,0,0,.12)}
.spread--outer{top:40px}
.spread--inner{top:620px}
.page{position:relative;width:410px;height:540px;background:var(--paper);overflow:hidden}
.brand{font-family:"Montserrat",Arial,sans-serif;font-weight:700;letter-spacing:.5px;display:flex;align-items:center;gap:6px;white-space:nowrap}
.brand__dot{width:9px;height:9px;border-radius:50%;background:currentColor;display:inline-block}

/* back cover */
.back{background:var(--paper-grey)}
.back__panel{position:absolute;left:0;top:22px;right:0;bottom:48px;background:var(--teal);color:#fff}
.back__brand{position:absolute;left:0;right:0;top:310px;justify-content:center;font-size:14px;color:#fff}
.back__title{position:absolute;left:0;right:0;top:336px;text-align:center;font-family:"Montserrat",sans-serif;font-weight:700;font-size:13px}
.back__rule{position:absolute;left:170px;width:70px;top:356px;height:1px;background:#fff}
.contact{position:absolute;top:374px;font-size:9px;line-height:1}
.contact--left{left:30px}
.contact--right{left:222px}
.contact__row{display:flex;align-items:flex-start;gap:7px;margin-bottom:9px}
.contact__row svg{flex:none}
.contact__hours{font-size:9px;line-height:1.35;margin-left:17px}
.contact__hours b{color:var(--ink);font-weight:600}

/* front cover */
.front__brand{position:absolute;right:26px;top:40px;font-size:19px;color:var(--teal)}
.front__photo{position:absolute;left:0;right:0;top:100px;height:250px;background:linear-gradient(135deg,#e9e6e1 0%,#cfd2d3 45%,#8f9aa6 100%)}
.front__band{position:absolute;left:0;right:0;top:350px;bottom:0;background:var(--teal);color:#fff;text-align:center}
.front__lead{font-family:"Montserrat",sans-serif;font-weight:500;font-size:24px;letter-spacing:1px;color:var(--ink);margin-top:24px}
.front__services{font-family:"Montserrat",sans-serif;font-weight:700;font-size:14px;line-height:1.3;margin:8px 30px 0}
.front__url{display:inline-block;margin-top:22px;border:1.5px solid #fff;padding:7px 16px;font-family:"Montserrat",sans-serif;font-weight:700;font-size:13px}

/* inner pages */
.inner{background:var(--paper);padding:0}
.statement{position:absolute;display:flex;height:54px}
.statement__tag{width:22px;background:var(--teal);color:#fff;font-family:"Montserrat",sans-serif;font-size:5.5px;font-weight:700;writing-mode:vertical-rl;transform:rotate(180deg);text-align:center;letter-spacing:.5px}
.statement__body{background:var(--slate);color:#f2f2f2;font-size:6px;line-height:1.45;padding:7px 9px;width:250px}
.statement--mission{left:22px;top:18px}
.statement--vision{left:138px;top:80px}
.h2{font-family:"Montserrat",sans-serif;font-weight:700;color:var(--teal);font-size:11px}
.body{font-size:6.8px;line-height:1.45;color:var(--ink)}
.left__block{position:absolute;left:22px;right:22px}
.step{display:flex;gap:9px;margin-top:9px}
.step__icon{flex:none;width:24px;height:24px;border-radius:50%;background:var(--teal);display:flex;align-items:center;justify-content:center}
.step__title{font-family:"Montserrat",sans-serif;font-weight:700;color:var(--teal);font-size:10px;margin-bottom:2px}
.footer{position:absolute;left:22px;right:22px;bottom:18px;height:30px}
.footer__brand{position:absolute;left:0;top:2px;font-size:9px;color:var(--teal)}
.footer__brand .brand__dot{width:7px;height:7px}
.footer__rule{position:absolute;left:180px;right:0;top:8px;height:1px;background:#9a9a9a}
.footer__url{position:absolute;right:16px;top:15px;background:var(--slate);color:#fff;font-size:6.5px;padding:3px 24px 3px 14px;border-radius:8px 0 0 8px}
.footer__num{position:absolute;right:0;top:11px;width:20px;height:20px;border-radius:50%;background:var(--teal);color:#fff;font-family:"Montserrat",sans-serif;font-weight:700;font-size:7.5px;display:flex;align-items:center;justify-content:center;border:2px solid #fff}
.right__block{position:absolute;left:24px;right:24px}
.right__block p{margin-top:6px}
.serve li{list-style:none;display:flex;gap:6px;margin-top:5px}
.diag{position:absolute;left:20px;right:20px;top:312px;height:170px;background:var(--paper-grey);padding:10px 14px}
.diag__title{text-align:center;font-family:"Montserrat",sans-serif;font-weight:700;color:var(--teal);font-size:10.5px;margin-bottom:8px}
.diag__cols{display:flex;justify-content:space-between}
.diag ul{list-style:none}
.diag li{display:flex;align-items:center;gap:6px;font-family:"Montserrat",sans-serif;font-weight:600;font-size:7px;margin-bottom:5px}
.diag li::before{content:"";width:11px;height:11px;border-radius:50%;background:var(--teal-soft);border:1.5px solid var(--teal);flex:none}
.diag__wide{margin-top:1px}
</style>
</head>
<body>

<section class="spread spread--outer">
  <article class="page back">
    <div class="back__panel">
      <div class="brand back__brand"><span class="brand__dot"></span>MERIDIAN REHAB PARTNERS</div>
      <div class="back__title">Contact Us</div>
      <div class="back__rule"></div>
      <div class="contact contact--left">
        <div class="contact__row"><svg width="10" height="10" viewBox="0 0 24 24"><path fill="#fff" d="M6.6 10.8a15 15 0 006.6 6.6l2.2-2.2a1 1 0 011-.25 11.4 11.4 0 003.6.6 1 1 0 011 1V20a1 1 0 01-1 1A17 17 0 013 4a1 1 0 011-1h3.5a1 1 0 011 1c0 1.25.2 2.45.6 3.6a1 1 0 01-.25 1z"/></svg>555-014-2200 / 555-014-2201</div>
        <div class="contact__row"><svg width="10" height="10" viewBox="0 0 24 24"><path fill="#fff" d="M2 5h20v14H2z"/><path fill="none" stroke="#6fa797" stroke-width="2" d="M2 5l10 8 10-8"/></svg>intake@meridianrehab.example</div>
        <div class="contact__row"><svg width="10" height="10" viewBox="0 0 24 24"><circle cx="12" cy="12" r="10" fill="none" stroke="#fff" stroke-width="2"/><path fill="none" stroke="#fff" stroke-width="1.6" d="M2 12h20M12 2c3 3 3 17 0 20M12 2c-3 3-3 17 0 20"/></svg>www.meridianrehab.example</div>
      </div>
      <div class="contact contact--right">
        <div class="contact__row"><svg width="10" height="10" viewBox="0 0 24 24"><path fill="#fff" d="M12 2a7 7 0 00-7 7c0 5 7 13 7 13s7-8 7-13a7 7 0 00-7-7zm0 9.5A2.5 2.5 0 1112 6.5a2.5 2.5 0 010 5z"/></svg><span style="line-height:1.35">1200 Linden Park Drive, Suite<br>300 Fairview, MI 48000</span></div>
        <div class="contact__hours"><b>Office Hours:</b> Monday – Friday<br>9:00 am – 4:30 pm<br><b>Therapy Hours:</b> By Appointment</div>
      </div>
    </div>
  </article>

  <article class="page front">
    <div class="brand front__brand"><span class="brand__dot"></span>MERIDIAN REHAB PARTNERS</div>
    <div class="front__photo" role="img" aria-label="Photo: therapist guiding a client through a stretching exercise on the floor of a bright living room"></div>
    <div class="front__band">
      <div class="front__lead">WE PROVIDE</div>
      <div class="front__services">OCCUPATIONAL THERAPY, SPEECH THERAPY<br>AND PSYCHOTHERAPY</div>
      <div class="front__url">www.meridianrehab.example</div>
    </div>
  </article>
</section>

<section class="spread spread--inner">
  <article class="page inner">
    <div class="statement statement--mission">
      <div class="statement__tag">MISSION STATEMENT</div>
      <div class="statement__body">Our mission is to provide high quality therapy that helps people recover skills in the places they live and work, so each client can return to a full, independent and meaningful life.</div>
    </div>
    <div class="statement statement--vision">
      <div class="statement__tag">VISION STATEMENT</div>
      <div class="statement__body">To be the trusted community partner for people healing after injury, known for caring clinicians, practical results and therapy that fits into everyday routines at home and at work.</div>
    </div>
    <div class="left__block" style="top:146px">
      <div class="h2">Who We Are</div>
      <p class="body">For over 25 years, our company has been using evidence-based principles of rehabilitation to assist patients with their recovery. We are out in the real world with patients every day, helping them to get their lives back. Our goal is to provide functional home and community-based therapy with a state-of-the-art approach, using the patient's natural environment such as their home.</p>
      <div class="h2" style="margin-top:7px">Finding success in the rehabilitative process relies<br>on certain key factors:</div>
      <div class="step"><div class="step__icon"><svg width="12" height="12" viewBox="0 0 24 24"><circle cx="12" cy="8" r="4" fill="#fff"/><path fill="#fff" d="M4 21c0-4.4 3.6-8 8-8s8 3.6 8 8z"/></svg></div><div><div class="step__title">Getting to Know You</div><p class="body">We do not set goals that are important to us, but rather we set goals that are important to you. We take input from you and the people you trust like your physician, case manager or perhaps a trusted family member.</p></div></div>
      <div class="step"><div class="step__icon"><svg width="12" height="12" viewBox="0 0 24 24"><circle cx="10" cy="10" r="6" fill="none" stroke="#fff" stroke-width="2.5"/><path stroke="#fff" stroke-width="3" d="M15 15l6 6"/></svg></div><div><div class="step__title">Comprehensive Evaluation</div><p class="body">We begin with an in-depth assessment with comprehensive evaluation protocols to determine your current level of functioning as compared to your prior level of functioning. We can then identify the areas that have been impacted and begin addressing them.</p></div></div>
      <div class="step"><div class="step__icon"><svg width="12" height="12" viewBox="0 0 24 24"><path fill="#fff" d="M5 3h14v18H5z"/><path stroke="#6fa797" stroke-width="2" d="M8 8h8M8 12h8M8 16h5"/></svg></div><div><div class="step__title">Creating and Implementing a Customized Rehabilitation Plan</div><p class="body">After the evaluation protocols are completed, a system of long-term and short-term goals are developed using our team approach. This allows for therapy to be tailored to your individual needs, and a plan of care is implemented based on your goals.</p></div></div>
      <div class="step"><div class="step__icon"><svg width="12" height="12" viewBox="0 0 24 24"><circle cx="12" cy="12" r="9" fill="none" stroke="#fff" stroke-width="2.5"/><circle cx="12" cy="12" r="3.5" fill="#fff"/></svg></div><div><div class="step__title">Focus on Accomplishments (Breaking Down Success):</div><p class="body">In order to facilitate progress toward patient goals, our therapy is most effective with consistent therapy appointments and repetition across therapy disciplines, which maximizes carry-over of new skills.</p></div></div>
    </div>
    <div class="footer">
      <div class="brand footer__brand"><span class="brand__dot"></span>MERIDIAN REHAB PARTNERS</div>
      <div class="footer__rule"></div>
      <div class="footer__url">www.meridianrehab.example</div>
      <div class="footer__num">01</div>
    </div>
  </article>

  <article class="page inner">
    <div class="right__block" style="top:24px">
      <div class="h2">Why Our Approach to Brain Injury is Unique</div>
      <p class="body">In more traditional therapy settings such as programs using outpatient models, attempts are made to simulate functional activities, combined with more structured tasks, all performed within the clinic environment. However, the inability to generalize learning has been shown to be a reoccurring difficulty for individuals with Traumatic Brain Injury and can often manifest in cognitive inflexibility, which makes carryover of learned skills to the real world a challenge.</p>
      <p class="body">Community-based treatment circumvents this difficulty by conducting therapy in the person's home, school, workplace, or other settings within their community, such as a grocery store or a post office. Clinicians are therefore able to witness first hand where a task is breaking down and can structure treatment accordingly. This allows for greater natural development of functional skills, with generalization issues no longer an obstacle toward meeting treatment goals.</p>
      <p class="body">At our practice we are committed to helping people recover their cognitive, physical and psychosocial abilities following brain injury through intensive individual treatment which focuses on safety, skill building and increasing independence. Our treatment approach is two-fold, with emphasis on direct restoration of brain functions and compensatory strategies such as planners, electronic reminders and organizational systems, introduced within a person's own relevant environments.</p>
      <div class="h2" style="margin-top:9px">Who We Serve</div>
      <ul class="serve body">
        <li><svg width="8" height="8" viewBox="0 0 24 24" style="flex:none;margin-top:1px"><rect x="1" y="1" width="22" height="22" fill="none" stroke="#6fa797" stroke-width="3"/><path fill="none" stroke="#6fa797" stroke-width="3" d="M6 12l4 4 8-8"/></svg>We treat adults and adolescents with a variety of diagnoses. We service home and community locations throughout Southeast and mid-Michigan.</li>
        <li><svg width="8" height="8" viewBox="0 0 24 24" style="flex:none;margin-top:1px"><rect x="1" y="1" width="22" height="22" fill="none" stroke="#6fa797" stroke-width="3"/><path fill="none" stroke="#6fa797" stroke-width="3" d="M6 12l4 4 8-8"/></svg>Our therapists hold a variety of certifications and endorsements including CBIS (Certified Brain Injury Specialist), NeuroSwallow, and VoiceStrong.</li>
      </ul>
    </div>
    <div class="diag">
      <div class="diag__title">Diagnoses can Include</div>
      <div class="diag__cols">
        <ul>
          <li>Traumatic Brain Injury</li>
          <li>Postconcussional Syndrome</li>
          <li>Spinal Cord Injury</li>
          <li>Post-traumatic Stress Disorder</li>
          <li>Depression</li>
          <li>Anxiety</li>
        </ul>
        <ul>
          <li>Mood Disorders</li>
          <li>Visual Impairments</li>
          <li>Balance Disorders</li>
          <li>Movement Disorders</li>
          <li>Neuromuscular Pathologies</li>
          <li>Dysphagia</li>
        </ul>
      </div>
      <ul class="diag__wide"><li>Musculoskeletal/Orthopedic injuries (ie. Spinal fractures/pathology, nerve injuries, pain)</li></ul>
    </div>
    <div class="footer">
      <div class="brand footer__brand"><span class="brand__dot"></span>MERIDIAN REHAB PARTNERS</div>
      <div class="footer__rule"></div>
      <div class="footer__url">www.meridianrehab.example</div>
      <div class="footer__num">02</div>
    </div>
  </article>
</section>

</body>
</html>
```